Flyer needed to promote gutter clearance service for established gardening company

We need a bright and engaging flyer to be designed to advertise our gutter clearance service.
Whilst we are a gardening company that normally does more horticultural work, during the winter we offer other services such as gutter clearance where we remove the debris from gutters and thereby reducing the risk of clogs, leakage, breakage and potential structural damage to the property.

Full details of our service, together with our overall brand and colours can be seen on www.marlowtreecare.co.uk/gutters.

We would like you to use the page on the website as a basis to create the flyer and so please feel free to use as much or as little of the wording contained within the webpage on the flyer drawing particular attention to "Prices starting at just £60 for an average 3 bed house". I will upload pictures but please feel free to use other graphics and fonts to make it stand out.

The contact details which should be included within the flyer are as follows:

Marlow Treecare Services Ltd
Orbit Trading Centre
Fairbrook Vale Ind Estate
Swindon
SN4 7HW

Tel: 01793 418302
www.marlowtreecare.co.uk
dean@marlowtreecare.co.uk

The flyers will eventually be printed out in A5 (210mm x 148mm) using Printelle and so needs to be in that size and suitable file for upload.

I have only put this as a 2 day project as its really urgent and I'm hoping we get some great designs in that time.

Target Market(s)

Homeowners between 25 - 65+

Industry/Entity Type

Home Improvement

Font styles to use
Serif
Sans Serif
Decorative
Script

Colors
6b449b
9bcb3c

Requirements
Must have
• Our colours are purple and green as seen on our website www.marlowtreecare.co.uk/gutters. Please use those colours.
• The flyer should draw attention to the following facts:
• We are Marlow Treecare Services Ltd (see attached logo)
• We are offering a Gutter Clearance Service in Swindon
• Prices start at just £60 for the average 3 bed house.
• We are fully insured.
• Our contact details must be included (as in the product description above)
• I have attached pictures but feel free to add other graphics or use fonts to make the flyer more engaging and interesting.
• Additional wording may be taken from the website at the address shown above. You can use as much or as little wording as you like just as long as the message gets across and the flyer contains our contact information and logo and the details shown above.
Nice to have
• I would like a bright and modern design which isn't too busy or cluttered. It should be something that is quick and easy to read.
Should not have
• I don't want it to look too busy or crowded with small type which people just won't read. Whilst I've said you can take whatever wording you want from our website, I'd suggest you don't take it all or too much. I want the main message (as detailed above in 'must haves') to stand out rather than have it contained deep within lots of small type face.

```html
<!DOCTYPE html>
<html lang="en">
<head>
<meta charset="utf-8">
<title>Gutter Clearance Services Flyer</title>
<link href="https://fonts.googleapis.com/css2?family=PT+Sans+Narrow:wght@400;700&family=PT+Sans:wght@700&display=swap" rel="stylesheet">
<style>
  :root {
    --purple: #6b449b;
    --green: #9bcb3c;
    --ink: #1d1d1b;
    --white: #ffffff;
  }
  * { margin: 0; padding: 0; box-sizing: border-box; }
  html, body { width: 1200px; height: 845px; overflow: hidden; background: var(--green); }
  .flyer {
    position: relative; width: 1200px; height: 845px; overflow: hidden;
    background: var(--green);
    font-family: "PT Sans Narrow", "Arial Narrow", sans-serif;
    font-size: 20px; line-height: 29px; text-align: center;
  }
  .photo { position: absolute; top: 0; height: 417px; overflow: hidden; }
  .photo-worker { left: 0; width: 393px; background: linear-gradient(135deg, #b24a3a 0%, #8a6a55 45%, #c77a2e 80%, #d9a441 100%); }
  .photo-before { left: 396px; width: 202px; background: linear-gradient(180deg, #6e7a5c 0%, #8a8464 45%, #5f6848 100%); }
  .photo-after { left: 601px; width: 200px; background: linear-gradient(180deg, #5b6a4a 0%, #b8b9b0 45%, #8c9088 100%); }
  .photo-leaves { left: 803px; width: 397px; background: linear-gradient(160deg, #7f9a3a 0%, #c9a640 40%, #4c4d50 75%, #3b3c3f 100%); }
  .photo-label {
    position: absolute; top: 8px; left: 0; right: 0;
    font-family: "PT Sans", Arial, sans-serif; font-weight: 700;
    font-size: 28px; line-height: 40px; color: var(--white); text-align: center;
  }
  .band {
    position: absolute; top: 418px; left: 0; width: 1200px; height: 46px;
    background: var(--purple); color: var(--white);
    font-family: "PT Sans", Arial, sans-serif; font-weight: 700; font-size: 29px; line-height: 46px;
  }
  .band-about { position: absolute; left: 0; width: 390px; }
  .band-services { position: absolute; left: 390px; width: 800px; }
  .col { position: absolute; white-space: nowrap; }
  .col-about { left: 10px; width: 390px; top: 468px; color: var(--ink); }
  .col-why { left: 400px; width: 396px; top: 467px; }
  .col-help { left: 822px; width: 394px; top: 467px; }
  .col-heading { color: var(--ink); font-weight: 400; font-size: 25px; line-height: 34px; }
  .col-body { color: var(--white); }
  .col-body + .col-body { margin-top: 14px; }
  .contact-box {
    position: absolute; left: 61px; top: 608px; width: 278px; height: 215px;
    background: var(--purple); color: var(--white); font-style: normal;
    padding-top: 7px; font-size: 20px; line-height: 28.7px; white-space: nowrap;
  }
  .price-box {
    position: absolute; left: 839px; top: 697px; width: 340px; height: 126px;
    background: var(--purple); color: var(--white);
    padding-top: 5px; font-size: 20px; line-height: 29.5px; white-space: nowrap;
    outline: 1px solid var(--white);
  }
</style>
</head>
<body>
<div class="flyer">
  <div class="photo photo-worker" role="img" aria-label="Worker in safety glasses clearing leaves from a gutter with a vacuum tube"></div>
  <div class="photo photo-before" role="img" aria-label="Gutter full of leaves and debris before clearing">
    <span class="photo-label">Before</span>
  </div>
  <div class="photo photo-after" role="img" aria-label="Clean empty gutter after clearing">
    <span class="photo-label">After</span>
  </div>
  <div class="photo photo-leaves" role="img" aria-label="Gloved hand removing autumn leaves from a roof gutter"></div>

  <div class="band">
    <span class="band-about">ABOUT</span>
    <span class="band-services">GUTTER CLEARANCE SERVICES</span>
  </div>

  <section class="col col-about">
    <p>Marlow Treecare Services in Swindon is a<br>well known and trusted local company and<br>can help you with safely clearing<br>your gutters this winter.</p>
  </section>

  <address class="contact-box">
    Marlow Treecare Services Ltd<br>
    Orbit Trading Centre<br>
    Fairbrook Vale Ind Estate<br>
    Swindon SN4 7HW<br>
    Tel: 01793 418302<br>
    www.marlowtreecare.co.uk<br>
    dean@marlowtreecare.co.uk
  </address>

  <section class="col col-why">
    <h2 class="col-heading">Why do my gutters need clearing?</h2>
    <p class="col-body">No matter what type of gutter you have,<br>they need to be cleaned at least once<br>per year. Whilst a gutter is very useful in<br>directing rainwater from your roof and<br>down the drain, it can accumulate leaves<br>and moss and other debris causing it to<br>clog and overflow or get broken.</p>
    <p class="col-body">Keeping them clean and clear is a great<br>way to avoid damage to your home,<br>causing potential health issues<br>to you and your family.</p>
  </section>

  <section class="col col-help">
    <h2 class="col-heading">How can we help?</h2>
    <p class="col-body">Clearing gutters is not just a dirty job but it<br>can be a dangerous one too if not done<br>properly.&nbsp; At Marlow Treecare Services,<br>we are fully insured and use the latest tools<br>and techniques to safely clear your gutters<br>and giving you peace of mind.</p>
  </section>

  <div class="price-box">
    And with prices starting at just £60 to clear<br>the gutters of an average 3 bed house,<br>it is an affordable way to get your home<br>prepared for the winter.
  </div>
</div>
</body>
</html>
```